Brightfield Power UK Flyer Design, for local domestic and commercial properties.

We are a renewable energy company called "BRIGHTFIELD POWER UK" we specialize in
Electrical and renewable energy project consultancy.
Solar panel installations
battery storage.
Electrical design and installation from Stage 3

Details can be found on our website: www.brightfieldpoweruk.co.uk
Am looking to have a flyer designed so we can have printed and delivered to all local areas.
We carry out free project surveys and offer full project transparency through out the clients journey.
attached is our logo of which i hope may help.

Target Market(s)

Domestic and commercial properties looking to dramatically reduce energy bills

Industry/Entity Type

Domestic, commercial, industrial, mixed used development and much more.

Font styles to use
Serif
Sans Serif
Decorative

Colors
FFC000
F8CF3A
FAE287
FDF2CF
FEFAEE
F0912C
F2A743
F7CA91
FBE8D2
FDF5EE
EE7325
F08F49
F5BC92
FAE3D3
FDF4ED

Requirements
Must have
• Highlight we offer free quotations and offer a fully transparent project processes from design, installation Plus leading health and safety process no matter what size project.
Nice to have
• Pictures of solar panel systems, i have attached a few pictures which you may wish to edit or take snippets etc.

```html
<!DOCTYPE html>
<html lang="en">
<head>
<meta charset="utf-8">
<title>Brightfield Power UK – Flyer</title>
<link rel="stylesheet" href="https://fonts.googleapis.com/css2?family=Poppins:wght@400;500;600;700&family=Tinos:wght@700&family=Oswald:wght@600;700&display=swap">
<style>
  :root{
    --orange:#F0912C;
    --orange-deep:#EE7325;
    --orange-light:#F2A743;
    --gold:#FFC000;
    --ink:#1b1b1b;
    --white:#ffffff;
    --black:#000000;
    --sky-pale:#e6f1fb;
  }
  *{margin:0;padding:0;box-sizing:border-box}
  html,body{width:976px;height:1200px;overflow:hidden;background:#fff}
  .flyer{position:relative;width:976px;height:1200px;overflow:hidden;font-family:"Poppins",sans-serif}
  .backdrop{position:absolute;inset:0}
  .layer{position:absolute}

  .brand{left:716px;top:118px;width:240px;text-align:center;color:var(--ink);font-family:"Poppins",sans-serif;font-weight:400;font-size:23px;line-height:1.25;letter-spacing:3px}

  .specialties-title{left:59px;top:84px;font-family:"Tinos",serif;font-weight:700;font-size:30px;color:var(--orange);letter-spacing:.5px}
  .specialties{left:59px;top:128px;list-style:none;color:var(--white);font-weight:500;font-size:25px;line-height:35px}
  .specialties li{display:flex;align-items:flex-start;margin-bottom:10px}
  .specialties li svg{flex:0 0 auto;width:52px;height:40px;margin-right:22px;margin-top:-2px}
  .specialties li:nth-child(1){margin-bottom:8px}

  .badge{left:702px;top:432px;width:180px;height:180px;border-radius:50%;display:flex;flex-direction:column;align-items:center;justify-content:center;color:var(--white);font-family:"Oswald",sans-serif;text-align:center}
  .badge .big{font-size:56px;font-weight:700;line-height:1;letter-spacing:1px}
  .badge .small{font-size:23px;font-weight:600;line-height:1.1;margin-top:4px}

  .benefits{left:59px;top:724px;list-style:none;color:var(--ink);font-size:33px;line-height:38px;width:760px}
  .benefits li{display:flex;align-items:flex-start;margin-bottom:14px}
  .benefits li svg{flex:0 0 auto;width:40px;height:40px;margin-right:20px;margin-top:0}

  .sectors{left:98px;top:1061px;width:772px;height:50px;background:var(--white);border:3px solid var(--orange);display:flex;align-items:center;justify-content:center;font-family:"Tinos",serif;font-weight:700;font-size:22px;color:var(--ink);letter-spacing:.3px}

  .contact{left:48px;top:1122px;display:flex;align-items:center;color:var(--white);height:52px}
  .contact .icon{width:44px;height:44px;margin-right:14px}
  .contact .phone{font-weight:600;font-size:32px;margin-right:18px}
  .contact .web{font-weight:700;font-size:32px;letter-spacing:1.5px}
</style>
</head>
<body>
<div class="flyer">
  <svg class="backdrop" width="976" height="1200" viewBox="0 0 976 1200" xmlns="http://www.w3.org/2000/svg">
    <defs>
      <linearGradient id="topPhoto" x1="0" y1="0" x2="0" y2="1">
        <stop offset="0" stop-color="#5d6266"/>
        <stop offset=".35" stop-color="#6c7070"/>
        <stop offset=".62" stop-color="#2f3d2a"/>
        <stop offset=".8" stop-color="#5a6670"/>
        <stop offset="1" stop-color="#8793a3"/>
      </linearGradient>
      <linearGradient id="lowerPhoto" x1="0" y1="0" x2="0" y2="1">
        <stop offset="0" stop-color="#cfe3f8"/>
        <stop offset=".45" stop-color="#e8f2fc"/>
        <stop offset=".7" stop-color="#d6e7f6"/>
        <stop offset=".78" stop-color="#6f9a4c"/>
        <stop offset=".86" stop-color="#3d5fa8"/>
        <stop offset="1" stop-color="#2a4c9a"/>
      </linearGradient>
      <linearGradient id="circleOne" x1="0" y1="0" x2="0" y2="1">
        <stop offset="0" stop-color="#9cc8ee"/>
        <stop offset=".45" stop-color="#2b2b35"/>
        <stop offset=".8" stop-color="#b58a63"/>
        <stop offset="1" stop-color="#8f6b4e"/>
      </linearGradient>
      <linearGradient id="circleTwo" x1="0" y1="0" x2="1" y2="1">
        <stop offset="0" stop-color="#a9cdee"/>
        <stop offset=".4" stop-color="#283448"/>
        <stop offset=".85" stop-color="#1d2738"/>
        <stop offset="1" stop-color="#b5634a"/>
      </linearGradient>
      <radialGradient id="badgeFill" cx=".4" cy=".35" r=".7">
        <stop offset="0" stop-color="#FFC000"/>
        <stop offset="1" stop-color="#EE7325"/>
      </radialGradient>
    </defs>

    <g role="img" aria-label="Photo: solar panels on a roof with trees under a cloudy sky">
      <path d="M0,0 H976 V470 Q420,560 0,700 Z" fill="url(#topPhoto)"/>
    </g>

    <path class="corner" d="M339,0 Q640,90 976,339 V0 Z" fill="var(--white)"/>
    <path class="swoosh" d="M230,0 H339 Q640,90 976,339 V352 Q600,70 230,0 Z" fill="var(--orange)"/>

    <g role="img" aria-label="Photo: installer fitting solar panels on a roof against a blue sky">
      <path d="M0,730 Q420,590 976,500 V1124 H0 Z" fill="url(#lowerPhoto)"/>
    </g>

    <path class="band" d="M0,694 Q420,556 976,466 V502 Q420,592 0,732 Z" fill="var(--orange)"/>

    <g role="img" aria-label="Photo: house roof with black solar panels and scaffolding">
      <circle cx="188" cy="583" r="110" fill="url(#circleOne)" stroke="var(--orange)" stroke-width="8"/>
    </g>
    <g role="img" aria-label="Photo: tiled roof with chimney and solar panels">
      <circle cx="473" cy="553" r="110" fill="url(#circleTwo)" stroke="var(--orange)" stroke-width="8"/>
    </g>

    <circle cx="792" cy="522" r="98" fill="none" stroke="var(--orange-light)" stroke-width="6" opacity=".7"/>
    <circle cx="792" cy="522" r="90" fill="url(#badgeFill)" stroke="var(--white)" stroke-width="3"/>

    <path class="footer-accent" d="M0,1080 Q420,1108 976,1104 V1126 H0 Z" fill="var(--orange)"/>
    <path class="footer" d="M0,1114 Q420,1120 976,1116 V1200 H0 Z" fill="var(--black)"/>

    <circle cx="836" cy="76" r="20" fill="var(--orange)"/>
  </svg>

  <div class="layer brand">BRIGHTFIELD<br>POWER UK</div>

  <h2 class="layer specialties-title">WE SPECIALIZE IN</h2>
  <ul class="layer specialties">
    <li>
      <svg viewBox="0 0 52 40"><circle cx="20" cy="20" r="16" fill="none" stroke="var(--orange)" stroke-width="3"/><path d="M23,8 L14,22 H20 L17,32 L27,17 H21 Z" fill="var(--orange)"/></svg>
      <span>Electrical and renewable<br>energy project consultancy.</span>
    </li>
    <li>
      <svg viewBox="0 0 52 40"><path d="M8,8 H38 L44,26 H2 Z" fill="none" stroke="var(--orange)" stroke-width="2.5"/><path d="M15,8 L13,26 M23,8 V26 M31,8 L34,26 M5,17 H41" stroke="var(--orange)" stroke-width="2"/><path d="M23,26 V34 M15,34 H31" stroke="var(--orange)" stroke-width="2.5"/><circle cx="44" cy="32" r="6" fill="none" stroke="var(--orange)" stroke-width="2.5"/></svg>
      <span>Solar panel installations</span>
    </li>
    <li>
      <svg viewBox="0 0 52 40"><rect x="2" y="9" width="40" height="22" rx="3" fill="none" stroke="var(--orange)" stroke-width="3"/><rect x="42" y="15" width="5" height="10" fill="var(--orange)"/><rect x="7" y="14" width="24" height="12" fill="var(--orange)"/></svg>
      <span>Battery storage.</span>
    </li>
    <li>
      <svg viewBox="0 0 52 40"><path d="M14,2 a12,12 0 0 1 8,21 V30 H8 V23 A12,12 0 0 1 14,2 Z" fill="none" stroke="var(--orange)" stroke-width="2.5"/><path d="M9,34 H21 M11,38 H19" stroke="var(--orange)" stroke-width="2.5"/><path d="M32,14 H46 V24 a7,7 0 0 1 -14,0 Z M36,8 V14 M42,8 V14 M39,31 V38" fill="none" stroke="var(--orange)" stroke-width="2.5"/></svg>
      <span>Electrical design &amp; installation<br>from Stage 3</span>
    </li>
  </ul>

  <div class="layer badge"><span class="big">FREE</span><span class="small">QUOTATIONS</span></div>

  <ul class="layer benefits">
    <li>
      <svg viewBox="0 0 40 40"><path d="M33,14 A15,15 0 1 1 26,7" fill="none" stroke="var(--orange)" stroke-width="3.5" stroke-linecap="round"/><path d="M12,19 L19,26 L35,8" fill="none" stroke="var(--orange)" stroke-width="3.5" stroke-linecap="round" stroke-linejoin="round"/></svg>
      <span>Free project surveys</span>
    </li>
    <li>
      <svg viewBox="0 0 40 40"><path d="M33,14 A15,15 0 1 1 26,7" fill="none" stroke="var(--orange)" stroke-width="3.5" stroke-linecap="round"/><path d="M12,19 L19,26 L35,8" fill="none" stroke="var(--orange)" stroke-width="3.5" stroke-linecap="round" stroke-linejoin="round"/></svg>
      <span>Fully transparent project, installation<br>&amp; health &amp; safety process no matter<br>what size project.</span>
    </li>
  </ul>

  <div class="layer sectors">DOMESTIC, COMMERCIAL, INDUSTRIAL PROPERTIES</div>

  <div class="layer contact">
    <svg class="icon" viewBox="0 0 44 44"><circle cx="22" cy="22" r="21" fill="var(--orange)"/><path d="M14,11 l5,-1 3,7 -3,3 q2,5 6,7 l3,-3 7,3 -1,5 q-2,3 -6,2 q-13,-5 -17,-17 q-1,-4 3,-6 Z" fill="var(--black)"/></svg>
    <span class="phone">936-555-0148</span>
    <svg class="icon" viewBox="0 0 44 44"><circle cx="22" cy="22" r="19" fill="none" stroke="var(--orange)" stroke-width="3.5"/><path d="M14,12 q6,2 5,7 q-4,2 -2,6 q3,2 1,7 M28,10 q-3,5 2,7 q5,0 6,5 M26,33 q1,-5 6,-6" fill="none" stroke="var(--orange)" stroke-width="2.5"/></svg>
    <span class="web">brightfieldpoweruk.co.uk</span>
  </div>
</div>
</body>
</html>
```